ClinicNerd Magazine Design for a digital monthly magazine

Designing an online magazine for monthly distribution. The magazine will be related to topics that are important to physicians. Finance, family, self-employment, medications, supplies, residency, continuing education, trends, advances, technology, etc. An example of another company that writes a monthly medical digital magazine editorial is Brevik Medical Post. Here is a link to one of their editions. https://flipsheet.example/brevikmedicalpost/docs/brv_april2021?fr=xQwErTyUiOp12345 I want our project to be more modern looking, less busy, and much more friendly to the eye. We have a website design project in process through ArtMosaic currently. I've spliced together some of our favorite parts of the designs that were submitted so far so you can have a vision for the theme, colors, and logos.
I’m looking for a template for the cover and inside page layout.

Target Market(s)

Physicians

Industry/Entity Type

Medical

Font styles to use
Other font styles liked:
• Rubik

Colors
0054AA
0677BA
7BADD7
CADEEF
E8F1F8
59FF00
82FF00
B8FF75
E3FFCB
F4FFEA

Requirements
Must have
• Project must be centered around Physicians. Discusses topics that are physician centric. Finance, family, medical supplies, insurance, billing, technology, private practice, employed practice, etc.
Nice to have
• The ability to create a 15 - 20 page monthly editorial from the design theme and structure that you create
Should not have
• should not bee to busy and flat looking. Must be modern and welcoming to the eye

```html
<!DOCTYPE html>
<html lang="en">
<head>
<meta charset="utf-8">
<title>Feature Spread – Physician Finance</title>
<link rel="stylesheet" href="https://fonts.googleapis.com/css2?family=Source+Sans+3:wght@200;300;400;700;900&display=swap">
<style>
  :root {
    --ink: #111111;
    --body-ink: #2b2b2b;
    --teal: #67aeaa;
    --paper: #ffffff;
    --device-light: #eef2f5;
    --device-mid: #cfd8de;
    --device-dark: #8f9aa2;
  }
  * { margin: 0; padding: 0; box-sizing: border-box; }
  html, body { width: 848px; height: 1200px; overflow: hidden; background: var(--paper); }
  .page {
    position: relative; width: 848px; height: 1200px; overflow: hidden;
    background: var(--paper);
    font-family: "Source Sans 3", "Source Sans Pro", sans-serif;
    color: var(--body-ink);
  }
  .article { position: absolute; left: 40px; width: 267px; }
  .article--first { top: 135px; }
  .article--second { top: 477px; }
  .article__kicker {
    font-weight: 300; font-size: 13px; letter-spacing: 0.2px;
    color: var(--ink); line-height: 20px;
  }
  .article__title {
    font-weight: 700; font-size: 13px; letter-spacing: 0.3px;
    color: var(--ink); line-height: 22px; margin-bottom: 0;
  }
  .article__body {
    font-weight: 300; font-size: 10.6px; line-height: 21.4px;
    text-align: justify; color: var(--body-ink);
  }
  .feature-visual {
    position: absolute; left: 354px; top: 110px; width: 420px; height: 800px;
  }
  .headline {
    position: absolute; left: 96px; top: 866px; width: 700px;
    line-height: 1; color: var(--ink);
  }
  .headline__light {
    display: block; font-weight: 200; font-size: 66px; letter-spacing: -0.5px;
  }
  .headline__bold {
    display: block; font-weight: 900; font-size: 98px; letter-spacing: -2px;
    margin-left: 266px; margin-top: -4px;
  }
  .headline__accent {
    display: block; font-weight: 900; font-size: 98px; letter-spacing: -2px;
    color: var(--teal); margin-top: -12px;
  }
  .folio {
    position: absolute; left: 782px; top: 338px; width: 30px;
    font-weight: 700; font-size: 19px; color: var(--ink);
    transform: rotate(90deg); transform-origin: center;
    text-align: center;
  }
  .folio-rule {
    position: absolute; left: 796px; top: 379px; height: 588px;
    border-left: 1.5px dotted var(--ink);
  }
  .running-title {
    position: absolute; left: 808px; top: 986px;
    font-weight: 300; font-size: 20px; color: var(--ink);
    transform: rotate(90deg); transform-origin: left top;
    white-space: nowrap;
  }
</style>
</head>
<body>
<main class="page">

  <section class="article article--first">
    <p class="article__kicker">NEMO ENIM IPSAM</p>
    <h2 class="article__title">VOLUPTATEM QUIA VOLUPTAS</h2>
    <p class="article__body">Et harum quidem rerum facilis est et expedita distinctio. Nam libero tempore, cum soluta nobis est eligendi optio cumque nihil impedit quo minus id quod maxime placeat facere possimus, omnis voluptas assumenda est, omnis dolor repellendus. Temporibus autem quibusdam et aut officiis debitis aut rerum necessitatibus saepe eveniet ut et voluptates repudiandae sint et molestiae non recusandae. Itaque earum rerum hic tenetur a sapiente delectus, ut aut reiciendis voluptatibus maiores alias consequatur aut per&shy;ferendis doloribus asperiores repellat. Sed ut perspiciatis unde omnis iste natus error sit voluptatem accusantium doloremque laudantium, totam rem aperiam, eaque ipsa quae ab illo invevitae dicta sunt explicabo.</p>
  </section>

  <section class="article article--second">
    <p class="article__kicker">NEMO ENIM IPSAM</p>
    <h2 class="article__title">VOLUPTATEM QUIA VOLUPTAS</h2>
    <p class="article__body">Nemo enim ipsam voluptatem quia voluptas sit aspernatur aut odit aut fugit, sed quia consequuntur magni dolores eos qui ratione voluptatem sequi nesciunt. Neque porro quisquam est, qui dolorem ipsum quia dolor sit amet, con&shy;sectetur, adipisci velit, sed quia non numquam eius modi tempora incidunt ut labore et dolore magnam aliquam quaerat voluptatem. Ut enim ad minima veniam, quis nos&shy;trum exercitationem ullam corporis suscipit laboriosam, nisi ut aliquid ex ea commodi consequatur? Quis autem vel eum iure reprehenderit qui in ea voluptate velit esse quam nihil molestiae consequatur, vel illum qui dolorem eum fugiat quo voluptas nulla pariatur? At vero eos et ac&shy;cusamus et iusto odio dignissimos ducimus qui blanditiis praesentium voluptatum deleniti atque corrupti quos do&shy;lores et quas molestias excepturi sint occaecati cupiditate</p>
  </section>

  <svg class="feature-visual" viewBox="0 0 420 800" role="img"
       aria-label="Photograph of a smartphone tilted in perspective, showing a finance app with mortgage and credit option cards">
    <defs>
      <linearGradient id="deviceTone" x1="0" y1="0" x2="1" y2="1">
        <stop offset="0" stop-color="var(--device-light)"/>
        <stop offset="0.6" stop-color="var(--device-mid)"/>
        <stop offset="1" stop-color="var(--device-dark)"/>
      </linearGradient>
      <linearGradient id="reflectionTone" x1="0" y1="0" x2="0" y2="1">
        <stop offset="0" stop-color="#e4e8eb"/>
        <stop offset="1" stop-color="#ffffff"/>
      </linearGradient>
    </defs>
    <path d="M95 120 Q110 40 190 25 L360 4 Q400 0 392 50 L300 640 Q290 690 240 700 L50 708 Q0 708 8 660 Z"
          fill="url(#deviceTone)"/>
    <path d="M30 720 L260 712 Q330 720 350 790 L40 800 Q20 760 30 720 Z" fill="url(#reflectionTone)"/>
  </svg>

  <h1 class="headline">
    <span class="headline__light">Topics important</span>
    <span class="headline__bold">physi-</span>
    <span class="headline__accent">cian finance.</span>
  </h1>

  <div class="folio">13</div>
  <div class="folio-rule"></div>
  <div class="running-title">runningTitle</div>

</main>
</body>
</html>
```